Scientific Web Site for TALQUIRE

Professional Scientific / Service orientated web site, motto, new logos attached for viewing.

"We measure so the Business Owner can Manage" their environments.
Site needs to be be mobile friendly.

We provide a service to electronically measure cleanliness of any surface and a value added disinfecting fogging surface.

Reports showing locations, trending, tracking and randomized test plans ongoing audits will be made available..

NOTE: Although image of Corona Virus is current we don't wont it plastered through the web site, their is more than the current virus.

Home Page - Professional Scientific / Service Looking
About
Our Approach
Services
Residential
Commercial
Transportation
Gyms
Educational & Daycare
Real Estate - Open for inspections, End of Lease etc

Contact
Mobile #
Email
Form to leave their details

Links to social media, Facebook, Instagram
Reference Sites: Ranked in preference
www.belunorm.com.au
https://www.vandrelhomecare.co.uk/
https://www.zelmarup.com/
https://www.ortivane.com.au/specialist-surface-disinfection/
https://www.plakorniv.com/design/48102937
https://www.plakorniv.com/design/59730418
https://www.plakorniv.com/design/41867205

Target Market(s)

Commercial and professional Services

Font styles to use
Sans Serif

Requirements
Must have
• Wix Website
Clean fresh look with appropriate imaging
Web site is a company advertising that will hold static information and we will market through social media.
Nice to have
• Scientific look and feel
Should not have
• Prominent Corona Virus images or references

```html
<!DOCTYPE html>
<html lang="en">
<head>
<meta charset="utf-8">
<title>Talquire – Disinfectant Fogging Services</title>
<link href="https://fonts.googleapis.com/css2?family=Catamaran:wght@400;500;600;700&family=Montserrat:wght@500;600&display=swap" rel="stylesheet">
<style>
:root{
  --orange:#f5821f;
  --charcoal:#333333;
  --ink:#1f1f2e;
  --navy:#0b1440;
  --footer:#2b2a2b;
  --footer-dark:#222122;
  --white:#ffffff;
  --muted:#555;
}
*{margin:0;padding:0;box-sizing:border-box}
html,body{width:1200px;height:3326px;overflow:hidden}
body{font-family:"Catamaran",sans-serif;color:var(--ink);background:var(--white);position:relative}
.abs{position:absolute}

/* header */
.site-header{position:absolute;left:0;top:0;width:1200px;height:116px;background:#fff;border-bottom:4px solid var(--orange)}
.brand{position:absolute;display:flex;align-items:center;gap:8px;font-weight:700;letter-spacing:4px;color:var(--ink)}
.brand .dot{width:14px;height:14px;border-radius:50%;background:var(--orange)}
.site-header .brand{left:120px;top:58px;font-size:28px}
.phone{position:absolute;right:123px;top:20px;font-size:17px;color:#444;display:flex;align-items:center;gap:8px}
.main-nav{position:absolute;right:120px;top:66px;display:flex;font-size:17px;color:#333}
.main-nav a{color:inherit;text-decoration:none;padding:0 26px;border-left:1px solid #aaa;line-height:16px}
.main-nav a:first-child{border-left:none}
.main-nav a:last-child{padding-right:0}

/* hero */
.hero{position:absolute;left:0;top:116px;width:1200px;height:656px;overflow:hidden;
  background:linear-gradient(180deg,#8ec4ea 0%,#d8ebf7 35%,#b9d6ea 60%,#4b7d8a 80%,#3d6b52 100%)}
.hero h1{position:absolute;left:0;width:1200px;top:82px;text-align:center;font-size:48px;line-height:58px;font-weight:700;color:#111}

/* why */
.why-title{position:absolute;left:0;width:1200px;top:806px;text-align:center;font-size:44px;font-weight:600;letter-spacing:-1px}
.why-intro{position:absolute;left:255px;width:690px;top:880px;text-align:center;font-size:14.5px;line-height:27px;color:#333}
.feature{position:absolute;width:461px;height:233px;color:#fff;padding:44px 40px 0 159px}
.feature.orange{background:var(--orange)}
.feature.dark{background:var(--charcoal)}
.feature h3{font-size:21px;font-weight:500;margin-bottom:10px}
.feature p{font-size:14.5px;line-height:24px}
.feature svg{position:absolute;left:40px;top:50px}

/* services */
.services{position:absolute;left:0;top:1640px;width:1200px;height:700px}
.services-bg{position:absolute;inset:0;background:radial-gradient(ellipse at 55% 55%,#1d3a7a 0%,#0d1a4e 45%,#070d2e 100%)}
.services h2{position:absolute;left:0;width:1200px;top:115px;text-align:center;color:#fff;font-size:44px;font-weight:600}
.services .tagline{position:absolute;left:0;width:1200px;top:172px;text-align:center;color:#fff;font-size:27px;font-weight:600}
.svc-label{position:absolute;font-family:"Montserrat",sans-serif;font-weight:600;color:#fff;font-size:19px;line-height:22px}
.svc-label.right{text-align:right}

/* about */
.about{position:absolute;left:0;top:2338px;width:1200px;height:630px;background:linear-gradient(120deg,#f7fafc 0%,#fbf6ef 35%,#eef8fb 70%,#dff2f4 100%)}
.about-card{position:absolute;left:336px;top:148px;width:528px;height:312px;background:#fff;border:2px solid var(--orange);border-radius:4px;padding:36px 56px}
.about-card h2{font-size:40px;font-weight:500;margin-bottom:14px}
.about-card p{font-size:16px;line-height:26px;color:#444;margin-bottom:18px}

/* footer */
.site-footer{position:absolute;left:0;top:2968px;width:1200px;height:300px;background:var(--footer);color:#fff}
.site-footer .brand{left:148px;top:142px;font-size:28px;color:#fff}
.social{position:absolute;left:178px;top:218px;display:flex;gap:24px}
.social span{width:20px;height:20px;border-radius:50%;background:#fff;display:block}
.f-col{position:absolute;top:88px;font-size:13px;line-height:24px}
.f-col h4{font-size:15px;font-weight:600;margin-bottom:8px}
.f-col .row{display:flex;gap:12px;align-items:flex-start;margin-bottom:10px;line-height:20px}
.contact-btn{position:absolute;left:862px;top:194px;width:176px;height:42px;background:var(--orange);color:#fff;font-size:16px;display:flex;align-items:center;padding-left:60px}
.contact-btn .ring{position:absolute;left:-2px;top:-2px;width:46px;height:46px;border-radius:50%;background:var(--footer);border:2px solid var(--orange);display:flex;align-items:center;justify-content:center}
.copyright{position:absolute;left:0;top:3268px;width:1200px;height:58px;background:var(--footer-dark);color:#fff;font-size:14px}
.copyright .left{position:absolute;left:142px;top:20px}
.copyright .right{position:absolute;right:130px;top:20px;font-size:13px}
</style>
</head>
<body>

<header class="site-header">
  <div class="brand"><span class="dot"></span>TALQUIRE</div>
  <div class="phone">
    <svg width="22" height="20" viewBox="0 0 22 20"><path d="M5 2l3 4-2 2c1 3 4 6 7 7l2-2 4 3-2 3C10 19 2 11 2 4z" fill="none" stroke="#666" stroke-width="1.5"/></svg>
    888.888.8888
  </div>
  <nav class="main-nav">
    <a href="#">Home</a><a href="#">About</a><a href="#">Our Approach</a><a href="#">Services ▾</a><a href="#">Contact Us</a>
  </nav>
</header>

<section class="hero">
  <div class="abs" role="img" aria-label="Sky with a molecular network pattern over a coastal city skyline" style="inset:0"></div>
  <h1>Disinfecant<br>Fogging Services</h1>
  <svg class="abs" style="left:0;top:0" width="1200" height="656" viewBox="0 0 1200 656">
    <g role="img" aria-label="Photo bubbles: city towers, campus buildings, gym workout, classroom and highway at night">
      <circle cx="295" cy="412" r="50" fill="#7e9bb5" stroke="#111" stroke-width="3"/>
      <circle cx="430" cy="440" r="58" fill="#4b74a8" stroke="#111" stroke-width="3"/>
      <circle cx="545" cy="355" r="86" fill="#7a9a6a" stroke="#111" stroke-width="3"/>
      <circle cx="735" cy="327" r="74" fill="#a89585" stroke="#111" stroke-width="3"/>
      <circle cx="565" cy="493" r="66" fill="#b9a58b" stroke="#111" stroke-width="3"/>
      <circle cx="720" cy="430" r="100" fill="#26336e" stroke="#111" stroke-width="3"/>
    </g>
    <circle cx="433" cy="324" r="19" fill="#f5821f"/>
    <circle cx="470" cy="522" r="17" fill="#f5821f"/>
    <circle cx="661" cy="547" r="18" fill="#f5821f"/>
    <path d="M0 656 Q600 580 1200 650 L1200 656 Z" fill="#fff"/>
    <path d="M0 650 Q600 580 1200 644" fill="none" stroke="#f5821f" stroke-width="6"/>
  </svg>
</section>

<h2 class="why-title">Why Choose Us</h2>
<p class="why-intro">Lorem Ipsum is simply dummy text of the printing and typesetting industry. Lorem Ipsum has been the industry's standard dummy text ever since the 1500s Lorem Ipsum is simply dummy text of the printing and typesetting industry.</p>

<div class="feature orange" style="left:129px;top:1004px">
  <svg width="80" height="80" viewBox="0 0 80 80"><circle cx="40" cy="20" r="15" fill="none" stroke="#fff" stroke-width="5"/><path d="M15 50a25 18 0 0 1 50 0" fill="none" stroke="#fff" stroke-width="5"/><g fill="#fff"><polygon points="14,52 17,60 25,60 19,65 21,73 14,68 7,73 9,65 3,60 11,60"/><polygon points="40,46 43,54 51,54 45,59 47,67 40,62 33,67 35,59 29,54 37,54"/><polygon points="66,52 69,60 77,60 71,65 73,73 66,68 59,73 61,65 55,60 63,60"/></g></svg>
  <h3>Customer Satisfaction</h3>
  <p>Lorem Ipsum is simply dummy text of the printing and typesetting industry. Lorem Ipsum has been the industry's standard dummy text ever.</p>
</div>
<div class="feature dark" style="left:610px;top:1004px">
  <svg width="80" height="80" viewBox="0 0 80 80"><circle cx="40" cy="30" r="24" fill="#fff"/><circle cx="40" cy="30" r="16" fill="none" stroke="#333" stroke-width="3"/><polygon points="40,20 43,27 50,27 44,32 46,39 40,35 34,39 36,32 30,27 37,27" fill="none" stroke="#333" stroke-width="2.5"/><path d="M22 46 12 72h16l6-16zM58 46l10 26H52l-6-16z" fill="#fff"/></svg>
  <h3>Quality</h3>
  <p>Lorem Ipsum is simply dummy text of the printing and typesetting industry. Lorem Ipsum has been the industry's standard dummy text ever.</p>
</div>
<div class="feature dark" style="left:129px;top:1255px">
  <svg width="100" height="100" viewBox="0 0 100 100" style="left:32px;top:48px"><circle cx="50" cy="46" r="22" fill="#fff"/><rect x="40" y="66" width="20" height="14" rx="3" fill="#fff"/><g stroke="#fff" stroke-width="5" stroke-linecap="round"><path d="M50 6v10M16 46H4M96 46H84M24 20l7 7M76 20l-7 7M24 72l7-7M76 72l-7-7"/></g></svg>
  <h3>Effective</h3>
  <p>Lorem Ipsum is simply dummy text of the printing and typesetting industry. Lorem Ipsum has been the industry's standard dummy text ever.</p>
</div>
<div class="feature orange" style="left:610px;top:1255px">
  <svg width="100" height="90" viewBox="0 0 100 90" style="left:35px;top:48px"><g stroke="#fff" stroke-width="3" fill="#fff"><circle cx="50" cy="45" r="11"/><circle cx="8" cy="60" r="5"/><circle cx="88" cy="45" r="3"/><circle cx="50" cy="8" r="4"/><circle cx="78" cy="78" r="4"/><path d="M50 12v22M40 50 13 58M61 45h24M58 53l17 22M14 8h10M30 8h6" fill="none"/></g></svg>
  <h3>Experienced</h3>
  <p>Lorem Ipsum is simply dummy text of the printing and typesetting industry. Lorem Ipsum has been the industry's standard dummy text ever.</p>
</div>

<section class="services">
  <div class="services-bg" role="img" aria-label="Dark blue digital tile backdrop with a faint molecular network"></div>
  <svg class="abs" style="left:0;top:0" width="1200" height="700" viewBox="0 0 1200 700">
    <path d="M0 0H1200V6Q600 36 0 6Z" fill="#fff"/>
    <path d="M0 10Q600 42 1200 10" fill="none" stroke="#5d5d62" stroke-width="9"/>
    <path d="M355 700A245 355 0 1 1 841 700" fill="none" stroke="#f5821f" stroke-width="14"/>
    <g fill="none" stroke="#f5821f" stroke-width="2.5">
      <path d="M227 313H375L425 342"/>
      <path d="M143 414H295L345 444"/>
      <path d="M125 540H275L325 575"/>
      <path d="M971 313H775L730 342"/>
      <path d="M1055 414H905L850 444"/>
      <path d="M1073 540H925L875 575"/>
    </g>
    <g fill="#fff" stroke="#f5821f" stroke-width="4">
      <circle cx="460" cy="375" r="38"/><circle cx="377" cy="478" r="38"/><circle cx="359" cy="608" r="38"/>
      <circle cx="739" cy="375" r="38"/><circle cx="816" cy="478" r="38"/><circle cx="840" cy="608" r="38"/>
    </g>
    <g role="img" aria-label="Line icons for each service" fill="none" stroke="#222" stroke-width="2">
      <rect x="446" y="360" width="26" height="28" rx="3"/><rect x="365" y="463" width="18" height="30"/><path d="M347 612l12-14 12 14v12h-24z"/>
      <circle cx="739" cy="368" r="6"/><path d="M730 392v-10h18v10"/><path d="M804 494v-16l12-10 12 10v16"/><rect x="826" y="596" width="28" height="24"/>
    </g>
    <path d="M531 700A67 67 0 0 1 665 700Z" fill="#6e7283" opacity=".85"/>
    <text x="598" y="680" text-anchor="middle" font-family="Catamaran, sans-serif" font-size="21" fill="#1b2248">+ More</text>
    <path d="M0 700V682Q600 650 1200 682V700Z" fill="#f6f8fa"/>
    <path d="M0 685Q600 652 1200 685" fill="none" stroke="#5d5d62" stroke-width="9"/>
  </svg>
  <h2>Our Most Valued Service</h2>
  <p class="tagline">We Measure so you can Manage</p>
  <div class="svc-label" style="left:227px;top:265px">Transportation<br>Services</div>
  <div class="svc-label" style="left:143px;top:366px">Commercial<br>Services</div>
  <div class="svc-label" style="left:125px;top:492px">Residential<br>Services</div>
  <div class="svc-label right" style="right:280px;top:288px">Gyms</div>
  <div class="svc-label right" style="right:145px;top:365px">Educational &amp;<br>Daycare</div>
  <div class="svc-label right" style="right:128px;top:514px">Real Estate</div>
</section>

<section class="about">
  <div class="about-card">
    <h2>About Us</h2>
    <p>Lorem Ipsum is simply dummy text of the printing and typesetting industry. Lorem Ipsum has been the industry's standard dummy text ever since the 1500s</p>
    <p>Lorem Ipsum is simply dummy text of the printing and typesetting industry. Lorem Ipsum has been the industry's standard dummy text ever since the 1500s</p>
  </div>
</section>

<footer class="site-footer">
  <div class="brand"><span class="dot"></span>TALQUIRE</div>
  <div class="social"><span></span><span></span><span></span></div>
  <div class="f-col" style="left:414px">
    <h4>Contact Us</h4>
    <div class="row"><svg width="14" height="18" viewBox="0 0 14 18"><path d="M7 17C2 10 1 8 1 6a6 6 0 0 1 12 0c0 2-1 4-6 11z" fill="none" stroke="#fff" stroke-width="1.4"/><circle cx="7" cy="6" r="2" fill="#fff"/></svg><span>27 Orrin Lane<br>Address 40218 TX</span></div>
    <div class="row"><svg width="16" height="16" viewBox="0 0 16 16"><path d="M3 1l3 4-2 2c1 2 3 4 5 5l2-2 4 3-2 3C7 15 1 9 1 3z" fill="#fff"/></svg><span>888.888.8888</span></div>
    <div class="row"><svg width="16" height="12" viewBox="0 0 16 12"><rect x="1" y="1" width="14" height="10" fill="none" stroke="#fff" stroke-width="1.4"/><path d="M1 1l7 6 7-6" fill="none" stroke="#fff" stroke-width="1.4"/></svg><span>name@talquire.com</span></div>
  </div>
  <div class="f-col" style="left:675px">
    <h4>Company</h4>
    <div>Home</div><div>About Us</div><div>Our Approach</div><div>Services</div><div>Contacts</div>
  </div>
  <div class="f-col" style="left:862px;font-size:14px;line-height:22px">
    <h4>Stil have questions?</h4>
    <div>A repesentative will aswer your<br>questions as soon as possible.</div>
  </div>
  <div class="contact-btn"><span class="ring"><svg width="20" height="20" viewBox="0 0 16 16"><path d="M3 1l3 4-2 2c1 2 3 4 5 5l2-2 4 3-2 3C7 15 1 9 1 3z" fill="none" stroke="#fff" stroke-width="1.3"/></svg></span>Contact Now</div>
</footer>
<div class="copyright">
  <span class="left">Copyright 2020 Talquire. All Rights Reserved.</span>
  <span class="right">Privacy Policy &nbsp;|&nbsp; Terms Of Services</span>
</div>

</body>
</html>
```